Dravell PowerPoint Theme/Template

I want to be able to put together presentations that have a cohesive look and work with my current branding on my website (www.dravell.com) and social media (#dravellskincare).

```html
<!DOCTYPE html>
<html lang="en">
<head>
<meta charset="utf-8">
<title>Dravell Presentation Title Slide</title>
<link href="https://fonts.googleapis.com/css2?family=Tinos:wght@700&family=Poppins:wght@400&display=swap" rel="stylesheet">
<style>
  :root {
    --bronze: #b1622b;
    --bronze-soft: #c07a45;
    --cream: #fcf3e6;
    --cream-warm: #f9e9d6;
    --blush: #f8e2d8;
    --ink-grey: #5a5450;
    --rule: #dcc3b3;
    --portrait-light: #ecd2bd;
    --portrait-mid: #d9b298;
    --portrait-hair: #9a9180;
  }
  * { margin: 0; padding: 0; box-sizing: border-box; }
  html, body {
    width: 1200px;
    height: 675px;
    overflow: hidden;
    background: var(--cream);
  }
  .slide {
    position: relative;
    width: 1200px;
    height: 675px;
    overflow: hidden;
    background:
      radial-gradient(ellipse 380px 260px at 70px 420px, rgba(248, 210, 200, 0.55), transparent 70%),
      radial-gradient(ellipse 420px 260px at 520px 260px, rgba(255, 255, 255, 0.85), transparent 70%),
      radial-gradient(ellipse 500px 300px at 300px 120px, rgba(250, 228, 212, 0.6), transparent 70%),
      linear-gradient(135deg, var(--cream-warm) 0%, var(--cream) 45%, #fbf1e4 100%);
  }
  .brand {
    position: absolute;
    left: 68px;
    top: 236px;
    width: 300px;
    text-align: center;
  }
  .brand-name {
    display: block;
    font-family: "Tinos", "Times New Roman", serif;
    font-weight: 700;
    font-size: 74px;
    line-height: 1;
    color: var(--bronze);
    letter-spacing: -1px;
  }
  .brand-tagline {
    display: block;
    margin-top: 8px;
    font-family: "Poppins", Arial, sans-serif;
    font-size: 19px;
    color: var(--bronze-soft);
    letter-spacing: 0.5px;
  }
  .title {
    position: absolute;
    left: 55px;
    top: 396px;
    font-family: "Tinos", "Times New Roman", serif;
    font-weight: 700;
    font-size: 47px;
    line-height: 1;
    color: var(--bronze);
    letter-spacing: 1.5px;
  }
  .subtitle {
    position: absolute;
    left: 55px;
    top: 470px;
    font-family: "Tinos", "Times New Roman", serif;
    font-weight: 700;
    font-size: 33px;
    line-height: 1;
    color: var(--bronze);
    letter-spacing: 1px;
  }
  .portrait {
    position: absolute;
    left: 690px;
    top: 60px;
    width: 380px;
    height: 597px;
    border-radius: 190px 190px 40px 40px;
    background:
      linear-gradient(180deg, var(--portrait-hair) 0%, var(--portrait-hair) 22%, var(--portrait-light) 34%, var(--portrait-mid) 100%);
    opacity: 0.85;
  }
  .footer-copyright {
    position: absolute;
    left: 20px;
    top: 647px;
    font-family: "Poppins", Arial, sans-serif;
    font-size: 14px;
    color: var(--ink-grey);
    line-height: 1;
  }
  .footer-rule {
    position: absolute;
    left: 170px;
    top: 656px;
    width: 1030px;
    height: 2px;
    background: var(--rule);
  }
</style>
</head>
<body>
  <div class="slide">
    <div class="brand">
      <span class="brand-name">Dravell</span>
      <span class="brand-tagline">by dr. maren okafor</span>
    </div>

    <h1 class="title">PROJECT TITLE HERE</h1>
    <h2 class="subtitle">SUBTEXT HERE</h2>

    <div class="portrait" role="img" aria-label="Portrait photo of a woman with slicked-back hair, split down the middle to show skin before and after treatment"></div>

    <p class="footer-copyright">Copyright text here</p>
    <div class="footer-rule"></div>
  </div>
</body>
</html>
```